MORVEN EHS & S Resources

We would like ArtHively to update and make our environmental, health and safety resources business website more professional and using our new logo and color scheme.
https://morvenehsresources.example/

```html
<!DOCTYPE html>
<html lang="en">
<head>
<meta charset="utf-8">
<title>MORVEN EHS &amp; S Resources</title>
<link href="https://fonts.googleapis.com/css2?family=Outfit:wght@400;500;600;800;900&display=swap" rel="stylesheet">
<style>
:root{
  --blue:#0aa5e6;
  --red:#e8202a;
  --ink:#111418;
  --text:#3a3d42;
  --grey:#efefef;
  --navy:#0b2a3f;
  --white:#ffffff;
  --line:#2c4a5e;
}
*{box-sizing:border-box;margin:0;padding:0}
html,body{width:1200px;height:2666px;overflow:hidden}
body{position:relative;background:var(--white);font-family:"Outfit",sans-serif;color:var(--ink)}
.abs{position:absolute}
a{color:inherit;text-decoration:none}

/* header */
.topbar{left:590px;top:0;width:610px;height:35px;background:var(--blue);clip-path:polygon(0 0,100% 0,100% 100%,20px 100%);color:var(--white);font-size:13px}
.topbar .item{position:absolute;top:9px;display:flex;align-items:center;gap:8px;white-space:nowrap}
.social-dot{position:absolute;top:7px;width:21px;height:21px;border-radius:50%;background:var(--white)}
.brand{left:141px;top:28px;font-size:40px;font-weight:800;letter-spacing:1px;color:var(--ink);display:flex;align-items:center;gap:12px}
.brand .mark{width:26px;height:26px;background:var(--red)}
.nav{top:58px;font-size:13px;color:var(--ink)}
.nav.active{color:var(--blue);font-weight:600}
.btn{display:flex;align-items:center;justify-content:center;color:var(--white);font-size:13px;border-radius:3px}
.btn-red{background:var(--red)}
.btn-blue{background:var(--blue)}

/* hero */
.hero{left:0;top:100px;width:1200px;height:530px;background:linear-gradient(90deg,#eaf3f9 0%,#dfeef7 40%,#b9d4e6 60%,#8b7a6a 75%,#c8743a 85%,#5d7fa0 100%)}
.hero-title{left:141px;top:200px;font-size:70px;font-weight:900;line-height:73px;color:var(--ink);letter-spacing:.5px}
.hero-title .accent{color:var(--red)}
.hero-sub{left:142px;top:431px;font-size:15px;font-weight:500}

/* about */
.eyebrow{font-size:15px;font-weight:500;color:var(--blue);letter-spacing:.3px}
.section-title{font-size:32px;font-weight:900;color:var(--ink)}
.about-text{left:634px;top:806px;width:430px;font-size:12.5px;line-height:23px;color:var(--text)}
.about-text p+p{margin-top:8px}

/* services */
.services{left:0;top:1178px;width:1200px;height:642px;background:var(--grey)}
.card{width:289px;height:115px;background:var(--white);border-bottom:3px solid var(--blue)}
.card-title{position:absolute;left:24px;top:58px;font-size:18px;font-weight:500;color:var(--ink)}
.card-tri{width:82px;height:72px}

/* cta */
.cta{left:141px;top:1905px;width:918px;height:317px;background:linear-gradient(90deg,#f08a2c 0%,#f4b33a 22%,#c7d9e6 48%,#d3e4f0 100%)}
.cta-title{left:669px;top:1988px;font-size:38px;font-weight:900;line-height:45px;color:var(--ink)}
.cta-title .accent{color:var(--red)}

/* footer */
.footer{left:0;top:2309px;width:1200px;height:357px;background:var(--navy);color:var(--white)}
.foot-head{font-size:18px;font-weight:600}
.foot-list{font-size:13px;line-height:25.5px}
.divider{width:1px;background:var(--line)}
.contact-row{font-size:13px;line-height:19px}
.contact-row strong{font-weight:600}
</style>
</head>
<body>

<!-- header -->
<div class="abs topbar">
  <div class="item" style="left:56px">
    <svg width="18" height="18" viewBox="0 0 24 24" fill="none" stroke="#fff" stroke-width="2"><path d="M5 3h4l2 5-2.5 1.5a11 11 0 0 0 6 6L16 13l5 2v4a2 2 0 0 1-2 2A17 17 0 0 1 3 5a2 2 0 0 1 2-2z"/></svg>
    <span>555.014.2290</span>
  </div>
  <div class="item" style="left:180px">
    <svg width="18" height="13" viewBox="0 0 24 16" fill="none" stroke="#fff" stroke-width="2"><rect x="1" y="1" width="22" height="14"/><path d="M1 1l11 8 11-8"/></svg>
    <span>info@morven.example</span>
  </div>
  <span class="social-dot" style="left:353px"></span>
  <span class="social-dot" style="left:384px"></span>
  <span class="social-dot" style="left:415px"></span>
  <span class="social-dot" style="left:446px"></span>
</div>

<div class="abs brand"><span class="mark"></span>MORVEN</div>

<a class="abs nav active" style="left:536px">Home</a>
<a class="abs nav" style="left:617px">About Us</a>
<a class="abs nav" style="left:718px">Our Services</a>
<a class="abs nav" style="left:838px">Security</a>
<a class="abs btn btn-red" style="left:932px;top:46px;width:127px;height:42px">Contact Us</a>

<!-- hero -->
<div class="abs hero" role="img" aria-label="Engineer holding a hard hat at an industrial site with technology overlay"></div>
<h1 class="abs hero-title">MORVEN EHS &amp;<br>SECURITY<br><span class="accent">RESOURCES</span></h1>
<p class="abs hero-sub">We have Education, Experience &amp; Credentials you can Trust!</p>
<a class="abs btn btn-blue" style="left:141px;top:473px;width:127px;height:42px">Contact Us</a>

<!-- about -->
<svg class="abs" style="left:146px;top:714px" width="437" height="379" viewBox="0 0 437 379" role="img" aria-label="Two colleagues reviewing plans, framed in a triangle">
  <defs>
    <linearGradient id="aboutFill" x1="0" y1="0" x2="1" y2="1">
      <stop offset="0" stop-color="#6f6a66"/>
      <stop offset=".5" stop-color="#b9b4ae"/>
      <stop offset="1" stop-color="#8c7a66"/>
    </linearGradient>
  </defs>
  <polygon points="218,0 437,379 0,379" fill="url(#aboutFill)"/>
</svg>
<div class="abs eyebrow" style="left:634px;top:742px">ABOUT US</div>
<h2 class="abs section-title" style="left:634px;top:758px">MORVEN EHS&amp;S RESOURCES</h2>
<div class="abs about-text">
  <p>MORVEN EHS &amp; Security resources is a woman-owned business providing EHS program development, training, consulting and skilled professional staffing.</p>
  <p>MORVEN was established to provide clients in all industries with safety, health, environmental, and security resources that have the experience necessary to meet unique client requirements. We utilize our extensive network of professional contacts and robust vetting process to bring forward top talent to carry out our client’s objectives.</p>
</div>
<a class="abs btn btn-red" style="left:634px;top:1021px;width:127px;height:42px">Read More</a>

<!-- services -->
<div class="abs services"></div>
<div class="abs eyebrow" style="left:0;width:1200px;text-align:center;top:1260px">WHAT WE DO</div>
<h2 class="abs section-title" style="left:0;width:1200px;text-align:center;top:1276px">OUR SERVICES</h2>

<div class="abs card" style="left:141px;top:1371px"><span class="card-title">EHS Consulting</span></div>
<div class="abs card" style="left:455px;top:1371px"><span class="card-title">Industrial Hygiene</span></div>
<div class="abs card" style="left:769px;top:1371px"><span class="card-title">Training</span></div>
<div class="abs card" style="left:141px;top:1547px"><span class="card-title">Occupational Health</span></div>
<div class="abs card" style="left:455px;top:1547px"><span class="card-title">Energy and Environment</span></div>
<div class="abs card" style="left:769px;top:1547px"><span class="card-title">Management Systems</span></div>

<svg class="abs card-tri" style="left:165px;top:1332px" viewBox="0 0 82 72"><polygon points="41,0 82,72 0,72" fill="var(--blue)"/></svg>
<svg class="abs card-tri" style="left:479px;top:1332px" viewBox="0 0 82 72"><polygon points="41,0 82,72 0,72" fill="var(--blue)"/></svg>
<svg class="abs card-tri" style="left:793px;top:1332px" viewBox="0 0 82 72"><polygon points="41,0 82,72 0,72" fill="var(--blue)"/></svg>
<svg class="abs card-tri" style="left:165px;top:1508px" viewBox="0 0 82 72"><polygon points="41,0 82,72 0,72" fill="var(--blue)"/></svg>
<svg class="abs card-tri" style="left:479px;top:1508px" viewBox="0 0 82 72"><polygon points="41,0 82,72 0,72" fill="var(--blue)"/></svg>
<svg class="abs card-tri" style="left:793px;top:1508px" viewBox="0 0 82 72"><polygon points="41,0 82,72 0,72" fill="var(--blue)"/></svg>

<a class="abs btn btn-red" style="left:537px;top:1693px;width:127px;height:42px">Read More</a>

<!-- call to action -->
<div class="abs cta" role="img" aria-label="Construction worker in hard hat and safety vest with a crane and building behind"></div>
<h2 class="abs cta-title">Smart Solutions<br>For Your <span class="accent">Business</span></h2>
<a class="abs btn btn-red" style="left:670px;top:2090px;width:127px;height:42px">Contact Us</a>

<!-- footer -->
<footer class="abs footer">
  <div class="abs" style="left:141px;top:130px;font-size:40px;font-weight:800;letter-spacing:1px">MORVEN</div>

  <div class="abs divider" style="left:362px;top:67px;height:177px"></div>
  <div class="abs divider" style="left:595px;top:67px;height:177px"></div>
  <div class="abs divider" style="left:910px;top:67px;height:177px"></div>

  <div class="abs foot-head" style="left:430px;top:76px">Quick Links</div>
  <div class="abs foot-list" style="left:430px;top:106px">
    <div>Home</div><div>About Us</div><div>Our Services</div><div>Security</div><div>Contact Us</div>
  </div>

  <div class="abs foot-head" style="left:663px;top:76px">Contact Details</div>
  <div class="abs contact-row" style="left:663px;top:108px;display:flex;gap:8px">
    <svg width="13" height="17" viewBox="0 0 12 16"><path d="M6 0a6 6 0 0 1 6 6c0 4-6 10-6 10S0 10 0 6a6 6 0 0 1 6-6z" fill="#fff"/><circle cx="6" cy="6" r="2.2" fill="var(--navy)"/></svg>
    <span>48, Harbor Lane, Suite 2<br>City, State XY 123456</span>
  </div>
  <div class="abs contact-row" style="left:663px;top:157px;display:flex;gap:9px">
    <svg width="13" height="13" viewBox="0 0 24 24" fill="#fff"><path d="M5 2h4l2 6-3 2a12 12 0 0 0 6 6l2-3 6 2v4a3 3 0 0 1-3 3A19 19 0 0 1 2 5a3 3 0 0 1 3-3z"/></svg>
    <span><strong>Phone</strong><br>555.014.2290</span>
  </div>
  <div class="abs contact-row" style="left:663px;top:207px;display:flex;gap:9px">
    <svg width="14" height="11" viewBox="0 0 24 16" style="margin-top:3px"><rect width="24" height="16" fill="#fff"/><path d="M1 1l11 8 11-8" fill="none" stroke="var(--navy)" stroke-width="2"/></svg>
    <span><strong>Email</strong><br>info@morven.example</span>
  </div>

  <div class="abs foot-head" style="left:977px;top:76px">Follow Us</div>
  <div class="abs foot-list" style="left:976px;top:106px;line-height:33px">
    <div style="display:flex;align-items:center;gap:9px"><span style="width:12px;height:12px;border-radius:50%;background:#fff"></span>Friendbook</div>
    <div style="display:flex;align-items:center;gap:9px"><span style="width:12px;height:12px;border-radius:50%;background:#fff"></span>ViewTube</div>
    <div style="display:flex;align-items:center;gap:9px"><span style="width:12px;height:12px;border-radius:50%;background:#fff"></span>Chirper</div>
    <div style="display:flex;align-items:center;gap:9px"><span style="width:12px;height:12px;border-radius:50%;background:#fff"></span>WorkLink</div>
  </div>

  <div class="abs" style="left:141px;top:311px;width:918px;height:1px;background:var(--line)"></div>
  <div class="abs" style="left:0;top:326px;width:1200px;text-align:center;font-size:13px">© 2024 Morven Ehs&amp;s Resources. All Rights Reserved.</div>
</footer>

</body>
</html>
```